Venture Capital Investment Firm

We are looking to overhaul our existing website (substantially), with only using the same logos (which we can provide).
We are an investment firm that focuses on making loans to late stage technology companies. Our site should ultimately look like other venture capital firms, and look modern and fresh. We have an existing website www.northvaleloan.com which this will be replacing, although we will be using a lot of the existing written content, and potentially the numbers of pages we will need, we are not wed to anything else. Please feel free to shoot any questions at any time and thank you in advance for your help!
Websites we like as examples:
https://www.tkbrandel.com/
https://www.emberwoodfunds.com/
Target Market(s)
Potential investors who will invest in our firm, as well as potentially companies that are looking to borrow money from us.

```html
<!DOCTYPE html>
<html lang="en">
<head>
<meta charset="utf-8">
<title>Northvale — Website Design</title>
<link href="https://fonts.googleapis.com/css2?family=Lato:wght@300;400;700&display=swap" rel="stylesheet">
<style>
  :root {
    --board-bg: #dff0fa;
    --ink-navy: #1b1a3f;
    --hero-navy: #1e1a45;
    --panel-navy: #221c4d;
    --brand-blue: #1f6fa8;
    --nav-blue: #2f8fd6;
    --link-cyan: #4cc6f5;
    --text-grey: #6b7079;
    --text-dark: #2b2e36;
    --rule: #e4e8ee;
    --blob: #eceef1;
    --white: #ffffff;
  }
  * { box-sizing: border-box; margin: 0; padding: 0; }
  html, body { width: 1200px; height: 1042px; overflow: hidden; }
  body {
    position: relative;
    background: var(--board-bg);
    font-family: 'Lato', sans-serif;
    color: var(--text-dark);
  }

  .board-title { position: absolute; left: 30px; top: 124px; }
  .board-title__name { font-size: 30px; font-weight: 400; color: var(--ink-navy); line-height: 1.2; }
  .board-title__sub { font-size: 30px; font-weight: 300; color: var(--brand-blue); line-height: 1.2; margin-top: 12px; }

  .dot-field {
    position: absolute;
    background: radial-gradient(circle, rgba(47,143,214,0.35) 1px, transparent 1.5px) 0 0 / 12px 12px;
  }
  .dot-field--top { left: 1036px; top: 52px; width: 126px; height: 140px; }
  .dot-field--left { left: 22px; top: 774px; width: 128px; height: 140px; }

  .site {
    position: absolute;
    left: 402px; top: 132px;
    width: 714px; height: 910px;
    background: var(--white);
    box-shadow: 8px 6px 20px rgba(30,60,100,0.12);
    overflow: hidden;
  }

  .hero {
    position: absolute; left: 0; top: 0; width: 714px; height: 408px;
    background:
      radial-gradient(ellipse at 55% 70%, rgba(40,110,210,0.55), transparent 60%),
      radial-gradient(ellipse at 90% 80%, rgba(50,120,220,0.45), transparent 50%),
      linear-gradient(180deg, var(--hero-navy) 0%, #1c2358 70%, #18305f 100%);
  }

  .brand {
    position: absolute; left: 59px; top: 16px;
    display: flex; align-items: center; gap: 7px;
  }
  .brand__mark { width: 18px; height: 18px; border-radius: 50%; background: var(--white); }
  .brand__name { font-size: 15px; font-weight: 400; color: var(--white); letter-spacing: 0.5px; }

  .main-nav { position: absolute; right: 58px; top: 20px; display: flex; gap: 14px; }
  .main-nav a { font-size: 9.5px; color: var(--nav-blue); text-decoration: none; text-transform: uppercase; }
  .main-nav a.is-current { color: var(--white); }

  .hero__headline {
    position: absolute; left: 63px; top: 156px; width: 360px;
    font-size: 24px; font-weight: 700; line-height: 30px; color: var(--white);
  }
  .hero__link {
    position: absolute; left: 323px; top: 222px;
    font-size: 17px; color: var(--link-cyan); text-decoration: underline;
  }

  .news-panel {
    position: absolute; left: 428px; top: 73px; width: 203px; height: 296px;
    background: rgba(34,28,77,0.92);
    padding: 20px 0 0 32px;
  }
  .news-panel__title { font-size: 11px; font-weight: 300; color: #c9cbe0; letter-spacing: 0.5px; margin-bottom: 10px; }
  .news-item { height: 63px; }
  .news-item__tag { font-size: 6.5px; color: var(--nav-blue); text-transform: uppercase; }
  .news-item__headline { font-size: 9px; font-weight: 300; color: #d8daea; line-height: 11.5px; margin-top: 5px; }
  .news-item__date { font-size: 6.5px; color: #7b7fa8; margin-top: 4px; }

  .art {
    position: absolute;
  }
  .section-title { position: absolute; font-size: 21px; font-weight: 300; color: var(--brand-blue); }
  .section-title--small { font-size: 17px; }
  .section-eyebrow { position: absolute; font-size: 11px; color: var(--text-dark); }
  .section-text { position: absolute; font-size: 9px; font-weight: 300; color: var(--text-grey); line-height: 14px; }
  .more-link {
    position: absolute; display: flex; align-items: center; gap: 7px;
    font-size: 9.5px; font-weight: 700; letter-spacing: 1px; color: var(--brand-blue);
    text-decoration: none; text-transform: uppercase;
  }
  .rule { position: absolute; height: 1px; background: var(--rule); }

  .photo-frame {
    position: absolute; left: 503px; top: 604px; width: 153px; height: 202px;
    border: 1px solid var(--rule); padding: 11px 10px;
  }
  .photo-frame__image {
    width: 100%; height: 100%;
    background: linear-gradient(135deg, #e8f0f5 0%, #cfdde7 50%, #6e8fa6 100%);
  }

  .site-footer { position: absolute; left: 60px; top: 836px; font-size: 9px; font-weight: 300; color: var(--text-grey); line-height: 11.5px; }
  .site-footer a { display: inline-block; margin-top: 5px; color: var(--brand-blue); }
</style>
</head>
<body>

  <header class="board-title">
    <h1 class="board-title__name">Northvale</h1>
    <p class="board-title__sub">Website Design</p>
  </header>

  <div class="dot-field dot-field--top" role="img" aria-label="Dot grid pattern"></div>
  <div class="dot-field dot-field--left" role="img" aria-label="Dot grid pattern"></div>

  <main class="site">
    <section class="hero" role="img" aria-label="Night city photo with glowing blue network lines">
      <div class="brand">
        <span class="brand__mark"></span>
        <span class="brand__name">NORTHVALE LOAN</span>
      </div>
      <nav class="main-nav">
        <a class="is-current" href="#">Home</a>
        <a href="#">Strategy</a>
        <a href="#">About Us</a>
        <a href="#">Team</a>
        <a href="#">News</a>
        <a href="#">Contact</a>
        <a href="#">Investors</a>
      </nav>

      <h2 class="hero__headline">We provide flexible capital to innovative companies and their investors</h2>
      <a class="hero__link" href="#">Learn more</a>

      <aside class="news-panel">
        <h3 class="news-panel__title">NEWS</h3>
        <article class="news-item">
          <p class="news-item__tag">Press Release</p>
          <p class="news-item__headline">Northvale Loan completes structured debt investment in Brightpath</p>
          <p class="news-item__date">APRIL 2018</p>
        </article>
        <article class="news-item">
          <p class="news-item__tag">Press Release</p>
          <p class="news-item__headline">Northvale Loan completes structured debt investment in Brightpath</p>
          <p class="news-item__date">APRIL 2018</p>
        </article>
        <article class="news-item">
          <p class="news-item__tag">Press Release</p>
          <p class="news-item__headline">Northvale Loan completes structured debt investment in Brightpath</p>
          <p class="news-item__date">APRIL 2018</p>
        </article>
        <article class="news-item">
          <p class="news-item__tag">Press Release</p>
          <p class="news-item__headline">Northvale Loan completes structured debt investment in Brightpath</p>
          <p class="news-item__date">APRIL 2018</p>
        </article>
      </aside>
    </section>

    <!-- Strategy -->
    <h2 class="section-title" style="left:60px; top:442px;">Our Strategy</h2>
    <p class="section-eyebrow" style="left:60px; top:490px;">PARTNERS FOR GROWTH</p>
    <p class="section-text" style="left:60px; top:516px; width:400px;">We are a global structured credit investment firm focused on the healthcare and technology industries.</p>
    <a class="more-link" href="#" style="left:364px; top:536px;">Learn more
      <svg width="14" height="14" viewBox="0 0 14 14"><circle cx="7" cy="7" r="6.2" fill="none" stroke="currentColor" stroke-width="1"/><path d="M4 7h6M7.5 4.5 10 7l-2.5 2.5" fill="none" stroke="currentColor" stroke-width="1"/></svg>
    </a>
    <div class="art" role="img" aria-label="Line illustration of a heartbeat heart beside a cloud and laptop" style="left:510px; top:466px; width:146px; height:86px; background:radial-gradient(ellipse at 50% 60%, var(--blob) 60%, transparent 62%);"></div>

    <div class="rule" style="left:55px; top:577px; width:602px;"></div>

    <!-- About -->
    <div class="art" role="img" aria-label="Line illustration of a brain and a light bulb" style="left:48px; top:597px; width:95px; height:77px; background:radial-gradient(ellipse at 50% 60%, var(--blob) 60%, transparent 62%);"></div>
    <h2 class="section-title section-title--small" style="left:160px; top:602px;">About Us</h2>
    <p class="section-text" style="left:160px; top:632px;">finance proven innovation with a different approach</p>
    <a class="more-link" href="#" style="left:356px; top:657px;">Learn more
      <svg width="14" height="14" viewBox="0 0 14 14"><circle cx="7" cy="7" r="6.2" fill="none" stroke="currentColor" stroke-width="1"/><path d="M4 7h6M7.5 4.5 10 7l-2.5 2.5" fill="none" stroke="currentColor" stroke-width="1"/></svg>
    </a>

    <div class="rule" style="left:55px; top:688px; width:440px;"></div>

    <!-- Team -->
    <div class="art" role="img" aria-label="Line illustration of puzzle pieces and a group of people" style="left:40px; top:708px; width:103px; height:72px; background:radial-gradient(ellipse at 50% 55%, var(--blob) 60%, transparent 62%);"></div>
    <h2 class="section-title section-title--small" style="left:161px; top:708px;">Our Team</h2>
    <p class="section-text" style="left:161px; top:738px;">Meet our team</p>
    <a class="more-link" href="#" style="left:357px; top:761px;">Learn more
      <svg width="14" height="14" viewBox="0 0 14 14"><circle cx="7" cy="7" r="6.2" fill="none" stroke="currentColor" stroke-width="1"/><path d="M4 7h6M7.5 4.5 10 7l-2.5 2.5" fill="none" stroke="currentColor" stroke-width="1"/></svg>
    </a>

    <figure class="photo-frame">
      <div class="photo-frame__image" role="img" aria-label="Photo of a stethoscope and pen on a medical chart"></div>
    </figure>

    <div class="rule" style="left:55px; top:818px; width:602px;"></div>

    <footer class="site-footer">
      <p>NORTHVALE LOAN, SAN FRANCISCO</p>
      <p>© 2015 Northvale Loan Partners LLC.&nbsp; All Rights Reserved.</p>
      <a href="#">Legal Disclaimer</a>
    </footer>
  </main>

</body>
</html>
```